Anzeigengestaltung für Stellenanzeige
Zielgruppe
Wir sind ein Abrechnungsunternehmen das für Zahnärzte die zahnmedizinische und zahntechnische Abrechnung von extern übernimmt.
Aufgrund einer Erweiterung suchen wir neues Personal welches uns unterstützt. Deshalb benötigen wir einen Stellenanzeige.
Wir suchen Personal - zahnmedizinische Fachangestellte mit Erfahrung in der Abrechnung
Abkürzungen: ZFA oder ZMV beides gewünscht wenn Abrechnungskenntnisse vorhanden sind.
Aufgabenstellung
Bitte Stellenanzeige unserer Website anpassen, www.zahnkanzleimerwen.de
logo bitte con Website übernehmen.
Moderne Gestaltung
Wir bieten:
-Anstellung Teilzeit oder Vollzeit
-Ein motiviertes und kompetentes Team
-Fort- und Weitermöglichkeiten
-Flexible Arbeits- und Urlaubszeiten
-Attraktive leistungsgerechte Bezahlung
Ihr Profil
Um die Stelle gut ausfüllen zu können, wünschen wir uns von Ihnen:
Abgeschlossene Ausbildung zum/zur Zahnmedizinische Fachangestellte, Zahnmedizinische Verwaltungsfachangestellte (m/w/d)
Selbstständiges Arbeiten und Einsatzbereitschaft
Gute PC-Kenntnisse und sicherer Umgang mit gängigen Office-Anwendungen
Erfahrung in der zahmedizinischen Abrechnung
Sorgfalt, Teamfähigkeit
Engagement und Freude am Beruf
Wir haben Ihr Interesse geweckt dann senden Sie uns Ihre Bewerbung an: t.brellmann@zahnkanzleimerwen.de
------Beispiel----------
Gerne auch eigene Beispiele....

```html
<!DOCTYPE html>
<html lang="de">
<head>
<meta charset="utf-8">
<title>Stellenanzeige – Zahnkanzlei Merwen</title>
<link rel="stylesheet" href="https://fonts.googleapis.com/css2?family=Montserrat:wght@300;400;500;600;700&display=swap">
<style>
  :root {
    --bg-dark: #121212;
    --bg-mid: #1d1d1d;
    --sand: #d5d1c7;
    --sand-text: #cbc5b8;
    --ink: #111111;
    --light: #e4e2de;
    --photo-a: #c9b49a;
    --photo-b: #2a2622;
  }
  * { margin: 0; padding: 0; box-sizing: border-box; }
  html, body { width: 850px; height: 1200px; overflow: hidden; background: var(--bg-dark); }
  body { font-family: "Montserrat", sans-serif; }
  .ad {
    position: relative;
    width: 850px; height: 1200px;
    background: radial-gradient(ellipse at 40% 30%, var(--bg-mid) 0%, var(--bg-dark) 70%);
    color: var(--light);
    overflow: hidden;
  }
  .brand {
    position: absolute; top: 40px; left: 0; width: 850px;
    text-align: center; color: var(--sand-text);
  }
  .brand-name { display: inline-flex; align-items: center; gap: 10px; font-size: 32px; font-weight: 500; letter-spacing: -0.5px; }
  .brand-dot { width: 14px; height: 14px; border-radius: 50%; background: var(--sand-text); }
  .brand-tagline { font-size: 13px; font-weight: 400; margin-top: 8px; }
  .headline-box {
    position: absolute; left: 21px; top: 140px; width: 812px; height: 170px;
    background: var(--sand); border-radius: 42px;
    color: var(--ink); text-align: center;
  }
  .headline-box h1 { font-size: 39px; font-weight: 600; margin-top: 20px; }
  .headline-box p { font-size: 16.5px; font-weight: 500; line-height: 23px; margin-top: 12px; }
  .section-title {
    position: absolute; left: 0; width: 850px; text-align: center;
    font-size: 35px; font-weight: 400; color: var(--sand-text);
  }
  .offer-title { top: 336px; }
  .profile-title { top: 546px; }
  .offer-list, .profile-text {
    position: absolute; left: 0; width: 850px; text-align: center;
    list-style: none; font-weight: 300; color: var(--light);
  }
  .offer-list { top: 393px; font-size: 18px; line-height: 24px; }
  .profile-text { top: 606px; font-size: 17px; line-height: 24px; }
  .profile-text p + p { margin-top: 24px; }
  .contact {
    position: absolute; left: 59px; top: 970px;
    font-size: 22.5px; line-height: 29px; font-weight: 400; color: var(--light);
  }
  .contact .email { color: var(--sand-text); font-weight: 300; }
  .team-photo {
    position: absolute; left: 575px; top: 855px; width: 242px; height: 274px;
    background: linear-gradient(180deg, var(--photo-a) 0%, var(--photo-b) 100%);
    border-radius: 6px; opacity: 0.85;
  }
</style>
</head>
<body>
<main class="ad">
  <header class="brand">
    <div class="brand-name"><span class="brand-dot"></span>Zahnkanzlei Merwen</div>
    <div class="brand-tagline">Zahnärztliche Abrechnung &amp; Managment</div>
  </header>

  <section class="headline-box">
    <h1>Wir suchen dich</h1>
    <p>- zahnmedizinische Fachangestellte mit Erfahrung in der Abrechnung<br>
    ZFA oder ZMV beides gewünscht<br>
    wenn Abrechnungskenntnisse vorhanden sind</p>
  </section>

  <h2 class="section-title offer-title">Wir bieten:</h2>
  <ul class="offer-list">
    <li>-Anstellung Teilzeit oder Vollzeit</li>
    <li>-Ein motiviertes und kompetentes Team</li>
    <li>-Fort- und Weitermöglichkeiten</li>
    <li>-Flexible Arbeits- und Urlaubszeiten</li>
    <li>-Attraktive leistungsgerechte Bezahlung</li>
  </ul>

  <h2 class="section-title profile-title">Ihr Profil:</h2>
  <div class="profile-text">
    <p>Um die Stelle gut ausfüllen zu können, wünschen wir uns von Ihnen:</p>
    <p>Abgeschlossene Ausbildung zum/zur Zahnmedizinische Fachangestellte,<br>
    Zahnmedizinische Verwaltungsfachangestellte (m/w/d)</p>
    <p>Selbstständiges Arbeiten und Einsatzbereitschaft<br>
    Gute PC-Kenntnisse und sicherer Umgang mit gängigen Office-Anwendungen<br>
    Erfahrung in der zahmedizinischen Abrechnung<br>
    Sorgfalt, Teamfähigkeit<br>
    Engagement und Freude am Beruf</p>
  </div>

  <div class="team-photo" role="img" aria-label="Foto von zwei Mitarbeiterinnen in beigen Blazern"></div>

  <footer class="contact">
    Wir haben Ihr Interesse geweckt dann<br>
    senden Sie uns Ihre Bewerbung an:<br>
    <span class="email">t.brellmann@zahnkanzleimerwen.de</span>
  </footer>
</main>
</body>
</html>
```